Business Cards for an 'affordable luxury' inner city home builder in Calgary.

We need a business card design that emulates the progressive, innovative, culture of our company and the modern style of our homes. Use our website www.velmarcrest-ab.com as a reference for the product we build.

Our company builds homes in the inner city space of Calgary, Alberta. We build affordable luxury.

Target Market(s)

Young professional Families

Contact Information for Business Card

Try to maintain consistency with the logo font and the card font.

Requirements
Must have
• The details must include: Name, education, title, phone number, website and email (Address is not as important)
• The design must be uniques (like our logo), elegant, sophisticated and modern.

```html
<!DOCTYPE html>
<html lang="en">
<head>
<meta charset="utf-8">
<title>Velmarcrest Homes Ltd – Business Card</title>
<link href="https://fonts.googleapis.com/css2?family=Montserrat:wght@500&family=Nunito:wght@400;600&display=swap" rel="stylesheet">
<style>
  :root {
    --backdrop: #2b2e34;
    --card: #ffffff;
    --ink: #3a3a3c;
    --ink-soft: #8e8e90;
    --rule: #4a4a4c;
  }
  html, body {
    margin: 0;
    padding: 0;
    width: 1200px;
    height: 800px;
    overflow: hidden;
    background: var(--backdrop);
  }
  .canvas {
    position: relative;
    width: 1200px;
    height: 800px;
  }
  .card {
    position: absolute;
    left: 390px;
    top: 75px;
    width: 420px;
    height: 650px;
    background: var(--card);
    box-shadow: 0 10px 30px rgba(0,0,0,0.35);
  }
  .brand-mark {
    position: absolute;
    right: 70px;
    top: 55px;
    width: 140px;
    height: 120px;
    display: flex;
    flex-direction: column;
    align-items: flex-end;
    justify-content: space-between;
    font-family: "Montserrat", sans-serif;
    font-weight: 500;
    font-size: 14px;
    letter-spacing: 0.12em;
    color: var(--ink);
    text-transform: uppercase;
  }
  .brand-mark .brand-square {
    width: 86px;
    height: 86px;
    background: var(--ink);
  }
  .company-name {
    position: absolute;
    left: 42px;
    top: 232px;
    margin: 0;
    font-family: "Montserrat", sans-serif;
    font-weight: 500;
    font-size: 24px;
    line-height: 1.2;
    letter-spacing: 0.06em;
    color: var(--ink);
    text-transform: uppercase;
  }
  .tagline {
    position: absolute;
    left: 42px;
    top: 355px;
    margin: 0;
    font-family: "Nunito", sans-serif;
    font-weight: 400;
    font-size: 22px;
    line-height: 1.45;
    color: var(--ink-soft);
  }
  .contact {
    position: absolute;
    left: 42px;
    top: 466px;
    margin: 0;
    font-family: "Nunito", sans-serif;
    font-weight: 600;
    font-size: 15.5px;
    line-height: 1.85;
    color: var(--ink);
  }
  .divider {
    position: absolute;
    left: 42px;
    top: 533px;
    width: 129px;
    height: 2px;
    background: var(--rule);
  }
  .address {
    position: absolute;
    left: 42px;
    top: 550px;
    margin: 0;
    font-family: "Nunito", sans-serif;
    font-weight: 400;
    font-size: 15.5px;
    line-height: 1.85;
    color: var(--ink);
    font-style: normal;
  }
</style>
</head>
<body>
  <main class="canvas">
    <section class="card">
      <div class="brand-mark">
        <span class="brand-square"></span>
        <span class="brand-name">Velmarcrest</span>
      </div>
      <h1 class="company-name">Velmarcrest<br>Homes Ltd</h1>
      <p class="tagline">We build<br>affordable<br>luxury homes.</p>
      <p class="contact">www.velmarcrest-ab.com<br>403-555-0148</p>
      <div class="divider"></div>
      <address class="address">248 14 Ave NE<br>Calgary, AB</address>
    </section>
  </main>
</body>
</html>
```